Domain Parking page and Listing page

1)
In need a design of a domain parking page, mainly with the same features as KOV.example as can be seen here: https://pickturnip.example/

2)
I need a design of a website with all domains listed. There's no company logo/name yet so it should be in plain font, for example "lotsbrim.example" (this is just an example), similar as:
https://kov.example/search?&terms=park&results=50&order_by=relevance

Delivery after approval in HTML/CSS. Should be responsive. Ideally use a framework like Bootstrap

Target Market(s)

Domain buyers, business owners

Industry/Entity Type

Business to business, Marketing, domains

Coding

Coded - Design and coding required

Number of Pages Required

2 page

Font styles to use
Sans Serif

Requirements
Must have
• Responsive design, worldly design.

```html
<!DOCTYPE html>
<html lang="en">
<head>
<meta charset="utf-8">
<title>lotsbrim.example – Domain search</title>
<link href="https://fonts.googleapis.com/css2?family=Poppins:wght@300;400;500;600&display=swap" rel="stylesheet">
<style>
:root{
  --page:#f7f7f7;
  --ink:#141414;
  --muted:#6b6b6b;
  --brand:#3a6daf;
  --field:#ffffff;
  --rule:#8a8a8a;
  --track:#c9c9c9;
  --foot-text:#ffffff;
  --foot-dim:#c9d7ea;
}
*{box-sizing:border-box;margin:0;padding:0}
html,body{width:1200px;height:902px;overflow:hidden}
body{background:var(--page);font-family:'Poppins',sans-serif;color:var(--ink);position:relative}
.abs{position:absolute}
.logo{left:102px;top:22px;font-size:25px;font-weight:500;letter-spacing:.3px}
.nav a{position:absolute;top:32px;font-size:14px;color:var(--ink);text-decoration:none;display:flex;align-items:center;gap:3px}
.nav svg{width:8px;height:8px}
.login{left:1037px;top:26px;width:63px;height:30px;border:1.5px solid var(--brand);border-radius:15px;color:var(--brand);font-size:14px;font-weight:600;display:flex;align-items:center;justify-content:center}
.search{left:252px;top:117px;width:695px;height:52px;background:var(--field);border-radius:26px;box-shadow:0 3px 8px rgba(0,0,0,.12)}
.tld{position:absolute;left:590px;top:16px;font-size:13.5px;display:flex;align-items:center;gap:3px}
.tld svg{width:8px;height:8px}
.search-icon{position:absolute;left:651px;top:14px;width:24px;height:24px}
.radio{display:flex;align-items:center;gap:6px;font-size:13.5px;white-space:nowrap}
.radio .dot{width:11px;height:11px;border:2px solid var(--ink);border-radius:50%;display:flex;align-items:center;justify-content:center}
.radio.on .dot::after{content:"";width:5px;height:5px;background:var(--ink);border-radius:50%}
.rule{height:1.5px;background:var(--rule)}
.section{font-size:13.5px;display:flex;justify-content:space-between;align-items:center;border-bottom:1.5px solid var(--rule);height:22px;padding-bottom:4px}
.section svg{width:8px;height:8px}
.field{background:var(--field);border-radius:17px;box-shadow:0 2px 6px rgba(0,0,0,.12);height:33px;font-size:16px;font-weight:300;padding-left:16px;display:flex;align-items:center}
.to{font-size:13.5px}
.track{height:2px;background:var(--track)}
.fill{height:2.5px;background:var(--brand)}
.knob{width:13px;height:13px;border-radius:50%;background:var(--brand)}
.footer{left:0;top:613px;width:1200px;height:289px;background:var(--brand);color:var(--foot-text)}
.footer .col-title{position:absolute;top:52px;font-size:11px;color:var(--foot-dim)}
.footer .link{position:absolute;font-size:12px}
.footer .fine{position:absolute;top:217px;font-size:11px;color:var(--foot-dim)}
.social{position:absolute;top:218px;width:12px;height:12px;border-radius:3px;background:var(--foot-dim)}
</style>
</head>
<body>
<header>
  <div class="abs logo">lotsbrim.example</div>
  <nav class="nav">
    <a style="left:432px">Buy a domain</a>
    <a style="left:561px">Sell your domain</a>
    <a style="left:707px">Learn <svg viewBox="0 0 10 10"><path d="M2 3.5l3 3 3-3" fill="none" stroke="currentColor" stroke-width="1.4"/></svg></a>
    <a style="left:783px">Company <svg viewBox="0 0 10 10"><path d="M2 3.5l3 3 3-3" fill="none" stroke="currentColor" stroke-width="1.4"/></svg></a>
  </nav>
  <div class="abs login">Login</div>
</header>

<main>
  <div class="abs search">
    <span class="tld">.com <svg viewBox="0 0 10 10"><path d="M2 3.5l3 3 3-3" fill="none" stroke="currentColor" stroke-width="1.4"/></svg></span>
    <svg class="search-icon" viewBox="0 0 24 24"><circle cx="13" cy="10" r="8" fill="none" stroke="var(--brand)" stroke-width="2"/><path d="M7.5 15.5L3 20" stroke="var(--brand)" stroke-width="2" stroke-linecap="round"/></svg>
  </div>

  <div class="abs radio on" style="left:252px;top:192px"><span class="dot"></span>Popular domain names</div>
  <div class="abs radio" style="left:507px;top:192px"><span class="dot"></span>3-letter domain names</div>
  <div class="abs radio" style="right:253px;top:192px"><span class="dot"></span>Premium domain names</div>
  <div class="abs rule" style="left:252px;top:233px;width:695px"></div>

  <div class="abs section" style="left:252px;top:258px;width:254px">Length <svg viewBox="0 0 10 10"><path d="M2 6.5l3-3 3 3" fill="none" stroke="currentColor" stroke-width="1.4"/></svg></div>
  <div class="abs section" style="left:692px;top:258px;width:255px">Price <svg viewBox="0 0 10 10"><path d="M2 6.5l3-3 3 3" fill="none" stroke="currentColor" stroke-width="1.4"/></svg></div>

  <div class="abs field" style="left:252px;top:298px;width:98px">1</div>
  <div class="abs to" style="left:372px;top:305px">to</div>
  <div class="abs field" style="left:408px;top:298px;width:98px">38</div>
  <div class="abs field" style="left:692px;top:298px;width:98px">0</div>
  <div class="abs to" style="left:813px;top:305px">to</div>
  <div class="abs field" style="left:849px;top:298px;width:98px">100000+</div>

  <div class="abs track" style="left:258px;top:351px;width:248px"></div>
  <div class="abs fill" style="left:258px;top:351px;width:162px"></div>
  <div class="abs knob" style="left:252px;top:345px"></div>
  <div class="abs knob" style="left:414px;top:345px"></div>

  <div class="abs fill" style="left:699px;top:351px;width:248px"></div>
  <div class="abs knob" style="left:693px;top:345px"></div>
  <div class="abs knob" style="left:941px;top:345px"></div>

  <div class="abs section" style="left:252px;top:377px;width:695px">Name <svg viewBox="0 0 10 10"><path d="M2 6.5l3-3 3 3" fill="none" stroke="currentColor" stroke-width="1.4"/></svg></div>

  <div class="abs radio on" style="left:252px;top:427px"><span class="dot"></span>No hyphens (-)</div>
  <div class="abs radio" style="left:523px;top:427px"><span class="dot"></span>No numerals (0-9)</div>
  <div class="abs radio" style="right:253px;top:427px"><span class="dot"></span>No special chars</div>

  <div class="abs section" style="left:252px;top:468px;width:254px">Starting with <svg viewBox="0 0 10 10"><path d="M2 6.5l3-3 3 3" fill="none" stroke="currentColor" stroke-width="1.4"/></svg></div>
  <div class="abs section" style="left:692px;top:468px;width:255px">Ending with <svg viewBox="0 0 10 10"><path d="M2 6.5l3-3 3 3" fill="none" stroke="currentColor" stroke-width="1.4"/></svg></div>
  <div class="abs field" style="left:252px;top:515px;width:254px"></div>
  <div class="abs field" style="left:693px;top:515px;width:254px"></div>
</main>

<footer class="abs footer">
  <div class="col-title" style="left:255px">Product</div>
  <div class="col-title" style="left:561px">Explore</div>
  <div class="col-title" style="left:871px">Company</div>
  <div class="link" style="left:255px;top:88px">Features</div>
  <div class="link" style="left:255px;top:121px">Pricing</div>
  <div class="link" style="left:255px;top:154px">Book a demo</div>
  <div class="link" style="left:561px;top:88px">Events</div>
  <div class="link" style="left:561px;top:121px">Blog</div>
  <div class="link" style="left:871px;top:88px">About us</div>
  <div class="link" style="left:871px;top:121px">Contact us</div>
  <div class="fine" style="left:255px">© 2023 Welcome. All right reserved.</div>
  <div class="fine" style="left:461px">Privacy Policy</div>
  <div class="fine" style="left:553px">Terms of Service</div>
  <span class="social" style="left:873px" aria-label="Video channel"></span>
  <span class="social" style="left:903px" aria-label="Microblog"></span>
  <span class="social" style="left:933px" aria-label="Professional network"></span>
</footer>
</body>
</html>
```